Design the app for the next NestLoop

We need a cutting edge, super UX-intuitive, design for a global parking app called Vamo.
- Homescreen and website have been finalised already (see attached pdf)
- Wireframed screens for the concepts we need have been provided in the attached pdf
- We need some really nice icons for parking space types, etc
- Needs to be very, very intuitive to use and navigate.
References: NestLoop app & Zolt app, for their simplicity of use
Updates
Project Deadline Extended
Reason: A few designers have requested that we extend this deadline. So here you go.
Industry/Entity Type
Parking
Look and feel
Each slider illustrates characteristics of the customer's brand and the style your logo design should communicate.

```html
<!DOCTYPE html>
<html lang="en">
<head>
<meta charset="utf-8">
<title>Add your space</title>
<link rel="stylesheet" href="https://fonts.googleapis.com/css2?family=Roboto:wght@400;500;700&display=swap">
<style>
  :root {
    --ink: #111111;
    --muted: #8a8a8a;
    --canvas: #f0f0f0;
    --surface: #ffffff;
    --line: #d8d8d8;
    --badge: #ececec;
    --chevron: #8f8f8f;
  }
  * { box-sizing: border-box; margin: 0; padding: 0; }
  html, body { width: 675px; height: 1200px; overflow: hidden; }
  body { font-family: 'Roboto', Arial, sans-serif; color: var(--ink); background: var(--canvas); }
  .screen { position: relative; width: 675px; height: 1200px; background: var(--canvas); overflow: hidden; }

  .status-bar { position: absolute; top: 0; left: 0; width: 675px; height: 39px; background: var(--surface);
    display: flex; align-items: center; font-size: 19px; font-weight: 500; padding: 0 10px; }
  .status-left { display: flex; align-items: center; gap: 8px; }
  .signal { display: flex; gap: 3px; }
  .signal span { width: 9px; height: 9px; border-radius: 50%; background: var(--ink); }
  .status-time { position: absolute; left: 0; right: 0; text-align: center; }
  .status-right { margin-left: auto; display: flex; align-items: center; gap: 6px; }
  .battery { width: 38px; height: 17px; border: 2px solid var(--ink); border-radius: 4px; padding: 2px; position: relative; }
  .battery::after { content: ""; position: absolute; right: -6px; top: 4px; width: 3px; height: 6px; background: var(--ink); border-radius: 0 2px 2px 0; }
  .battery i { display: block; width: 22%; height: 100%; background: var(--ink); }

  .nav-bar { position: absolute; top: 39px; left: 0; width: 675px; height: 91px; background: var(--surface);
    border-bottom: 1px solid var(--line); box-shadow: 0 3px 5px rgba(0,0,0,0.12); }
  .nav-back { position: absolute; left: 26px; top: 30px; }
  .nav-title { position: absolute; left: 0; right: 0; top: 30px; text-align: center; font-size: 26px; font-weight: 700; }
  .nav-preview { position: absolute; left: 518px; top: 18px; width: 132px; height: 59px; border: 1px solid var(--line);
    border-radius: 3px; display: flex; align-items: center; justify-content: center; font-size: 22px; background: var(--surface); }

  .steps { position: absolute; top: 156px; left: 0; width: 675px; list-style: none; }
  .step { height: 78px; margin-bottom: 16px; background: var(--surface); display: flex; align-items: center;
    position: relative; box-shadow: 0 2px 3px rgba(0,0,0,0.08); }
  .step-number { position: absolute; left: 31px; width: 36px; height: 36px; border-radius: 50%; background: var(--badge);
    display: flex; align-items: center; justify-content: center; font-size: 22px; color: var(--ink); }
  .step-label { position: absolute; left: 117px; font-size: 26px; font-weight: 500; }
  .step-chevron { position: absolute; right: 26px; top: 27px; }
  .step.is-active { background: var(--ink); color: var(--surface); }
  .step.is-active .step-number { background: var(--surface); color: var(--ink); font-weight: 500; }
  .step.is-active .step-label { font-weight: 400; }

  .preview-button { position: absolute; left: 28px; top: 1037px; width: 622px; height: 60px; background: var(--surface);
    border: 1px solid var(--line); border-radius: 4px; display: flex; align-items: center; justify-content: center; font-size: 22px; }

  .tab-bar { position: absolute; left: 0; top: 1108px; width: 675px; height: 92px; background: var(--surface);
    border-top: 1px solid var(--line); display: flex; }
  .tab { flex: 1; display: flex; flex-direction: column; align-items: center; padding-top: 14px; color: var(--muted); font-size: 19px; }
  .tab svg { height: 44px; margin-bottom: 6px; }
  .tab.is-current { color: var(--ink); font-weight: 700; }
</style>
</head>
<body>
<div class="screen">
  <header class="status-bar">
    <div class="status-left">
      <div class="signal"><span></span><span></span><span></span><span></span><span></span></div>
      <span>ORBIT</span>
      <svg width="22" height="16" viewBox="0 0 22 16"><path d="M1 5a15 15 0 0 1 20 0M4.5 8.5a10 10 0 0 1 13 0M8 12a5 5 0 0 1 6 0" fill="none" stroke="#111" stroke-width="2.2" stroke-linecap="round"/><circle cx="11" cy="14.5" r="1.5" fill="#111"/></svg>
    </div>
    <div class="status-time">4:21 PM</div>
    <div class="status-right">
      <svg width="12" height="20" viewBox="0 0 12 20"><path d="M1 5l10 9-5 4V2l5 4L1 15" fill="none" stroke="#111" stroke-width="1.6"/></svg>
      <span>22%</span>
      <div class="battery"><i></i></div>
    </div>
  </header>

  <nav class="nav-bar">
    <svg class="nav-back" width="22" height="36" viewBox="0 0 22 36"><path d="M19 3L4 18l15 15" fill="none" stroke="#555" stroke-width="4"/></svg>
    <h1 class="nav-title">Add your space</h1>
    <div class="nav-preview">Preview</div>
  </nav>

  <ol class="steps">
    <li class="step is-active">
      <span class="step-number">1</span><span class="step-label">Describe your space</span>
      <svg class="step-chevron" width="16" height="26" viewBox="0 0 16 26"><path d="M3 2l10 11L3 24" fill="none" stroke="#fff" stroke-width="3.5"/></svg>
    </li>
    <li class="step">
      <span class="step-number">2</span><span class="step-label">Select Feaures</span>
      <svg class="step-chevron" width="16" height="26" viewBox="0 0 16 26"><path d="M3 2l10 11L3 24" fill="none" stroke="#8f8f8f" stroke-width="3"/></svg>
    </li>
    <li class="step">
      <span class="step-number">3</span><span class="step-label">Add Photo</span>
      <svg class="step-chevron" width="16" height="26" viewBox="0 0 16 26"><path d="M3 2l10 11L3 24" fill="none" stroke="#8f8f8f" stroke-width="3"/></svg>
    </li>
    <li class="step">
      <span class="step-number">4</span><span class="step-label">Choose Availability</span>
      <svg class="step-chevron" width="16" height="26" viewBox="0 0 16 26"><path d="M3 2l10 11L3 24" fill="none" stroke="#8f8f8f" stroke-width="3"/></svg>
    </li>
    <li class="step">
      <span class="step-number">5</span><span class="step-label">Set Price</span>
      <svg class="step-chevron" width="16" height="26" viewBox="0 0 16 26"><path d="M3 2l10 11L3 24" fill="none" stroke="#8f8f8f" stroke-width="3"/></svg>
    </li>
  </ol>

  <div class="preview-button">Preview your space</div>

  <footer class="tab-bar">
    <div class="tab is-current">
      <svg width="44" height="44" viewBox="0 0 44 44"><path d="M6 16L22 4l16 12" fill="none" stroke="#111" stroke-width="3"/><path d="M9 38V26l4-8h18l4 8v12h-6v-4H15v4z" fill="#111"/><rect x="15" y="21" width="14" height="5" fill="#fff"/><circle cx="14" cy="30" r="2.2" fill="#fff"/><circle cx="30" cy="30" r="2.2" fill="#fff"/></svg>
      <span>Find a Space</span>
    </div>
    <div class="tab">
      <svg width="44" height="44" viewBox="0 0 44 44"><rect x="5" y="7" width="34" height="32" rx="2" fill="none" stroke="#8a8a8a" stroke-width="3"/><rect x="5" y="7" width="34" height="8" fill="#8a8a8a"/><path d="M13 3v8M31 3v8" stroke="#8a8a8a" stroke-width="3"/><path d="M14 27l6 6 11-12" fill="none" stroke="#8a8a8a" stroke-width="3.5"/></svg>
      <span>Booking</span>
    </div>
    <div class="tab">
      <svg width="44" height="44" viewBox="0 0 44 44"><path d="M4 14L22 4l18 10" fill="none" stroke="#8a8a8a" stroke-width="3"/><rect x="8" y="16" width="28" height="24" fill="none" stroke="#8a8a8a" stroke-width="3"/><path d="M12 22h20M12 27h20M12 32h20M12 37h20" stroke="#8a8a8a" stroke-width="2.5"/></svg>
      <span>Your Spaces</span>
    </div>
    <div class="tab">
      <svg width="44" height="44" viewBox="0 0 44 44"><circle cx="22" cy="12" r="9" fill="#8a8a8a"/><path d="M7 42V32c0-6 5-10 15-10s15 4 15 10v10z" fill="#8a8a8a"/></svg>
      <span>Profile</span>
    </div>
  </footer>
</div>
</body>
</html>
```